Savour and Thrive Wellbeing is being Launched and needs a business card and stationery package

I need a stationery package including business card (primary focus) , letterhead, digital letterhead, envelopes, with compliments slip, A 5 note sheet for the rebranding of my business and launch of my new website. I have a logo, like beige, brown earthy tones with a hint of red. I would also like the option of my letterhead also being printed on recycled paper in another format as well as the traditional letterhead. I do also send my letters to GPs and specialists digitally as well. I like to stand out from the usual stereotype of fruits and vegetables on business cards as I find that quite tacky and stereotypical. I want the business card to capture the essence of my logo as natural, nutrition, enjoyment, nurturing and freedom with food. I have attached the logo, and additional brief sheet on my ideas. Happy to have any background that is complementary to my theme, and what you believe would be catching. Definitely DONT'T like pink, try to pick up the darker colour in the logo please. and think too much black is a little overpowering.

Target Market(s)

clients who are interested in improving their health and wellness. Client 80% females; 20% males

Industry/Entity Type

Health And Wellness

Contact Information for Business Card

I am open to having different backgrounds as well that would complement the logo. Probably less emphasis on the heart out of the logo - just happy to keep that in the logo only please
I am also wanting two business cards - one for the appointments, one for general distribution and media distribution (both need to look consistent though) - but does give opportunity for one of the business cards to be less wordy and more striking. And the front of the business card can certainly stand out with the entire savour and thrive logo and my name and grab the attention of the receiver.
1st business card
on front:
Lorena Whitcombe
Savour and Thrive Wellbeing & logo
Nutritionist and Dietitian
Tarvel Medical Centre
647 Brindle Hill Rd, Quorrel Q 4987
Phone: (07) 3017 2968 Fax: (07) 3156 7209
Mobile: 0400 261 937
www.savourandthrivewellbeing.example.au
lorena@savourandthrivewellbeing.example.au
on back:
next appointment

……………………….. at ……………………… (possibly 4 times)
If you are unable to keep your appointment, please contact us as soon as possible (small font)
2nd business card (needs to be very eye catching and stand out)
on front: Savour and Thrive Wellbeing logo and my name
on back:
Lorena Whitcombe
address
phones, fax, website, email address

Font styles to use
Other font styles liked:
• please refer to logo

Requirements
Must have
• refreshing and simple; new and vibrant - I am rebranding my business after 20 years
• to get a feel of what is the theme - go to my new website (not completed as yet - but you will get a preliminary view) - don't do as google search as blocked - but can put into website header and it will be shown
• www.savourandthrivewellbeing.example.au - but please ignore the colouring of the 4 blocks under the slider on the home page - I am not wanting these colourings - they are getting updated.
Nice to have
• earthy tones, beige, hint of red, fonts to match logo if possible, organic, modern
• get inspiration from my logo please, open to having other backgrounds that complement
Should not have
• no food shots or stereotypical weight/ scales images
• no green, yellow or orange

```html
<!DOCTYPE html>
<html lang="en">
<head>
<meta charset="utf-8">
<title>Savour and Thrive Wellbeing – Business Cards</title>
<link rel="stylesheet" href="https://fonts.googleapis.com/css2?family=Open+Sans:wght@400;600&family=Dancing+Script:wght@600&display=swap">
<style>
  :root {
    --backdrop: #ebebeb;
    --card: #ffffff;
    --ink: #2e2e2e;
    --ink-soft: #555555;
    --accent: #b0525a;
    --rule: #9a9a9a;
  }
  * { box-sizing: border-box; margin: 0; padding: 0; }
  html, body {
    width: 1200px; height: 900px; overflow: hidden;
    background: var(--backdrop);
    font-family: "Open Sans", Arial, sans-serif;
    color: var(--ink);
  }
  .sheet {
    position: relative; width: 1200px; height: 900px;
    display: flex; align-items: center; justify-content: center; gap: 60px;
  }
  .card {
    position: relative; width: 525px; height: 300px;
    background: var(--card);
    box-shadow: 0 10px 28px rgba(0,0,0,0.12);
  }

  /* Front */
  .holder { position: absolute; left: 34px; top: 40px; }
  .holder-name {
    font-family: "Dancing Script", cursive; font-weight: 600;
    color: var(--accent); font-size: 24px; line-height: 1.1; margin-bottom: 4px;
  }
  .holder-details { font-size: 11.5px; line-height: 1.45; color: var(--ink-soft); }

  .brand {
    position: absolute; right: 40px; top: 92px;
    display: flex; align-items: center; gap: 10px;
  }
  .brand-dot { width: 20px; height: 20px; border-radius: 50%; background: var(--accent); }
  .brand-name { font-size: 21px; font-weight: 400; color: var(--ink); letter-spacing: 0.3px; }

  .contacts {
    position: absolute; right: 30px; bottom: 24px;
    list-style: none; text-align: right;
    font-size: 11px; line-height: 1.5; color: var(--ink-soft);
  }
  .contacts li { display: flex; justify-content: flex-end; align-items: center; gap: 6px; }
  .contacts svg { width: 10px; height: 10px; fill: var(--accent); flex: none; }
  .contacts .no-icon { padding-right: 16px; }

  /* Back */
  .appt-title {
    position: absolute; left: 0; right: 0; top: 34px;
    text-align: center; font-size: 24px; font-weight: 400; color: var(--ink);
  }
  .appt-rows { position: absolute; left: 48px; right: 48px; top: 96px; }
  .appt-row {
    display: flex; align-items: flex-end; gap: 12px;
    height: 30px; font-size: 11px; color: var(--ink-soft);
  }
  .appt-line { flex: 1; border-bottom: 1px dotted var(--rule); height: 14px; }
  .appt-note {
    position: absolute; left: 0; right: 0; bottom: 26px;
    text-align: center; font-size: 9.5px; color: var(--ink-soft);
  }
</style>
</head>
<body>
<main class="sheet">

  <section class="card card-front" aria-label="Business card front">
    <div class="holder">
      <p class="holder-name">Lorena Whitcombe</p>
      <p class="holder-details">Nutritionist and Dietitian<br>Tarvel Medical Centre<br>647 Brindle Hill Rd,<br>Quorrel Q 4987</p>
    </div>

    <div class="brand">
      <span class="brand-dot"></span>
      <span class="brand-name">Savour and Thrive Wellbeing</span>
    </div>

    <ul class="contacts">
      <li>(07) 3017 2968
        <svg viewBox="0 0 10 10" aria-hidden="true"><path d="M2 0.5 L3.6 0.5 L4.2 3 L3 3.8 Q4 6 6.2 7 L7 5.8 L9.5 6.4 L9.5 8 Q9.5 9.5 8 9.5 Q0.5 9 0.5 2 Q0.5 0.5 2 0.5Z"/></svg>
      </li>
      <li>(07) 3156 7209
        <svg viewBox="0 0 10 10" aria-hidden="true"><rect x="2.5" y="0.5" width="5" height="3"/><rect x="0.5" y="3.5" width="9" height="4.5" rx="1"/><rect x="2.5" y="7" width="5" height="2.5"/></svg>
      </li>
      <li>0400 261 937
        <svg viewBox="0 0 10 10" aria-hidden="true"><path d="M2.5 0 H7.5 Q8 0 8 0.5 V9.5 Q8 10 7.5 10 H2.5 Q2 10 2 9.5 V0.5 Q2 0 2.5 0Z M3 1.2 V7.8 H7 V1.2Z"/></svg>
      </li>
      <li class="no-icon">www.savourandthrivewellbeing.example.au</li>
      <li>lorena@savourandthrivewellbeing.example.au
        <svg viewBox="0 0 10 10" aria-hidden="true"><path d="M0.5 2 H9.5 V8 H0.5Z M1.2 2.6 L5 5.6 L8.8 2.6" stroke="#fff" stroke-width="0.8"/></svg>
      </li>
    </ul>
  </section>

  <section class="card card-back" aria-label="Business card back">
    <h2 class="appt-title">Your Next Appointment</h2>
    <div class="appt-rows">
      <div class="appt-row"><span class="appt-line"></span><span>at</span><span class="appt-line"></span></div>
      <div class="appt-row"><span class="appt-line"></span><span>at</span><span class="appt-line"></span></div>
      <div class="appt-row"><span class="appt-line"></span><span>at</span><span class="appt-line"></span></div>
      <div class="appt-row"><span class="appt-line"></span><span>at</span><span class="appt-line"></span></div>
    </div>
    <p class="appt-note">If you are unable to keep your appointment, please contact us as soon as possible</p>
  </section>

</main>
</body>
</html>
```